need professional, precise design for a website

I will start with a homepage design and if we pick your design, we'll have you design up to 6 more interior pages (we'll pay extra for these of course). We need a homepage design for a reserve study company based in Idaho, covering the northwest region. The company is called copper ridge reserve study. Their current site is at https://www.copperridgereserves.example/ and they really like this site for inspiration https://www.fundplannerhub.example/ but they would like an original design, just more modern and fresh like the sample site. I have logo files I will attach. They want something that looks financial and has a feel of accuity. Their main call to action will be to have someone fill in a contact form or call them on the phone. They will have a sample study that someone can download as on the fundplannerhub site. You can use copy from their current site.

```html
<!DOCTYPE html>
<html lang="en">
<head>
<meta charset="utf-8">
<title>Copper Ridge Reserves – Association Analytics</title>
<link href="https://fonts.googleapis.com/css2?family=Figtree:wght@300;400;500;700&display=swap" rel="stylesheet">
<style>
  :root {
    --page-bg: #dcdcdc;
    --brand-purple: #2a0f78;
    --white: #ffffff;
    --ink: #333333;
    --ink-soft: #555555;
    --footer-bg: #333333;
    --footer-ink: #a9a9a9;
    --sky: #8a8c8a;
    --city: #6d6a66;
    --trees: #3f4a30;
    --trees-dark: #2c3523;
  }
  * { box-sizing: border-box; margin: 0; padding: 0; }
  html, body { width: 1200px; height: 1134px; overflow: hidden; }
  body {
    background: var(--page-bg);
    font-family: "Figtree", "Helvetica Neue", Arial, sans-serif;
    color: var(--ink);
    position: relative;
  }
  .hero {
    position: absolute; left: 84px; top: 0; width: 1022px; height: 608px;
    border-radius: 0 0 17px 17px; overflow: hidden;
  }
  .hero-photo {
    position: absolute; inset: 0;
    background: linear-gradient(180deg, var(--sky) 0%, #7b7d7a 30%, var(--city) 42%, #4d5540 52%, var(--trees) 70%, var(--trees-dark) 100%);
  }
  .hero-shade { position: absolute; inset: 0; background: rgba(0,0,0,0.12); }
  .brand { position: absolute; top: 18px; left: 0; right: 0; text-align: center; }
  .brand-name { color: var(--brand-purple); font-weight: 700; font-size: 39px; line-height: 46px; }
  .brand-tag { color: var(--white); font-weight: 700; font-size: 41px; line-height: 50px; }
  .phone {
    position: absolute; right: 10px; top: 100px; color: var(--white);
    font-size: 19px; display: flex; align-items: center; gap: 7px;
  }
  .main-nav {
    position: absolute; left: 0; right: 0; top: 128px; height: 28px;
    border-bottom: 1px solid rgba(255,255,255,0.55);
  }
  .main-nav a {
    position: absolute; top: 0; color: var(--white); text-decoration: none;
    font-size: 19px; line-height: 26px; letter-spacing: 0.3px;
  }
  .main-nav a.active { border-bottom: 2px solid var(--white); }
  .hero-copy { position: absolute; top: 268px; left: 0; right: 0; text-align: center; color: var(--white); }
  .hero-copy h1 { font-weight: 300; font-size: 31px; line-height: 40px; }
  .hero-cta {
    display: inline-block; margin-top: 16px; border: 2px solid var(--white);
    color: var(--white); text-decoration: none; font-weight: 300;
    font-size: 31px; line-height: 36px; padding: 1px 6px;
  }
  .arrow { position: absolute; top: 312px; }
  .dots { position: absolute; top: 562px; left: 0; right: 0; display: flex; justify-content: center; gap: 7px; }
  .dot { width: 26px; height: 26px; border: 2px solid var(--white); border-radius: 50%; position: relative; }
  .dot.active::after { content: ""; position: absolute; inset: 4px; background: var(--white); border-radius: 50%; }
  .service {
    position: absolute; top: 629px; height: 427px; background: var(--white);
    border-radius: 17px;
  }
  .service h2 {
    text-align: center; font-weight: 500; font-size: 19px; line-height: 22px;
    margin-top: 13px; color: var(--ink);
  }
  .service-photo {
    width: 227px; height: 96px; border-radius: 8px; margin: 17px auto 0;
  }
  .service p {
    position: absolute; top: 160px; font-weight: 300; font-size: 15.3px;
    line-height: 20.5px; color: var(--ink-soft);
  }
  .service .more {
    position: absolute; top: 381px; left: 50%; transform: translateX(-50%);
    border: 2px solid var(--ink); padding: 0 6px; color: var(--ink);
    text-decoration: none; font-size: 19px; line-height: 25px; white-space: nowrap;
  }
  .site-footer {
    position: absolute; left: 0; top: 1074px; width: 1200px; height: 60px;
    background: var(--footer-bg); color: var(--footer-ink);
    display: flex; align-items: center; justify-content: center; gap: 10px;
    font-size: 16px; font-weight: 300;
  }
</style>
</head>
<body>
  <header class="hero">
    <div class="hero-photo" role="img" aria-label="City skyline above a wide park of green trees under an overcast sky"></div>
    <div class="hero-shade"></div>
    <div class="brand">
      <div class="brand-name">Copper Ridge Reserves</div>
      <div class="brand-tag">Association Analytics</div>
    </div>
    <div class="phone">
      <svg width="20" height="20" viewBox="0 0 24 24" fill="none" stroke="#fff" stroke-width="1.6" stroke-linecap="round" stroke-linejoin="round"><path d="M5 3h3l2 5-2.5 1.5a11 11 0 0 0 6 6L15 13l5 2v3a2 2 0 0 1-2 2A16 16 0 0 1 3 5a2 2 0 0 1 2-2z"/><path d="M15 3a6 6 0 0 1 6 6M15 7a2 2 0 0 1 2 2"/></svg>
      (208) 555-0142
    </div>
    <nav class="main-nav">
      <a class="active" href="#" style="left:239px">HOME</a>
      <a href="#" style="left:338px">ABOUT OUR COMPANY</a>
      <a href="#" style="left:613px">RESERVE STUDIES</a>
    </nav>
    <div class="hero-copy">
      <h1>Your financial road map for the next 30 years!</h1>
      <a class="hero-cta" href="#">Contact us</a>
    </div>
    <svg class="arrow" style="left:42px" width="30" height="52" viewBox="0 0 30 52"><path d="M27 2 3 26l24 24" fill="none" stroke="#fff" stroke-width="2.5"/></svg>
    <svg class="arrow" style="left:952px" width="30" height="52" viewBox="0 0 30 52"><path d="M3 2l24 24L3 50" fill="none" stroke="#fff" stroke-width="2.5"/></svg>
    <div class="dots">
      <span class="dot active"></span><span class="dot"></span><span class="dot"></span><span class="dot"></span>
      <span class="dot"></span><span class="dot"></span><span class="dot"></span><span class="dot"></span>
    </div>
  </header>

  <section class="service" style="left:84px;width:306px">
    <h2>HOA &amp; Condominium Studies</h2>
    <div class="service-photo" role="img" aria-label="Row of brick and sided townhomes with trees" style="background:linear-gradient(180deg,#9fb0b8 0%,#a06a50 45%,#7a4a38 75%,#6c6a5a 100%)"></div>
    <p style="left:23px;width:266px">Every homeowners association is different. Different sets of assets, different financials and different historical backgrounds that have brought you to the present. Each of these is taken into consideration to customize your 30 year budget and build the most accurate, most precise long-term savings ("reserve") report you can buy.</p>
    <a class="more" href="#">View More</a>
  </section>

  <section class="service" style="left:416px;width:358px">
    <h2>Commercial, Vacation &amp; Time Share</h2>
    <div class="service-photo" role="img" aria-label="Modern red brick and glass office building" style="background:linear-gradient(90deg,#5a5d66 0%,#8a4a44 35%,#6b3a36 65%,#3e4452 100%)"></div>
    <p style="left:50px;width:262px">Your property represents a significant capital investment. In many cases, your business is dependent on the livelihood and functionality of the edifice in which it resides. We believe a fiscally sound plan and budget of capital expenses is as essential as the building itself. We are comprehensive, thorough and intense about our calculations.</p>
    <a class="more" href="#">View More</a>
  </section>

  <section class="service" style="left:799px;width:306px">
    <h2>Parks &amp; Public Lands</h2>
    <div class="service-photo" role="img" aria-label="Green park with tall trees and a playground" style="background:linear-gradient(180deg,#4d6b3a 0%,#3c5a2c 50%,#6a9a3c 80%,#78a844 100%)"></div>
    <p style="left:23px;width:266px">Much like HOA's and condominiums, you have finite funds that originate from a constituent base of tax payers. Planning the use of these funds and repairs and/or maintenance of public assets is essential to transparency and candid communication with your constituents. Being in control of the future starts with a financial plan.</p>
    <a class="more" href="#">View More</a>
  </section>

  <footer class="site-footer">
    <svg width="24" height="24" viewBox="0 0 24 24" fill="none" stroke="#a9a9a9" stroke-width="2"><circle cx="12" cy="12" r="10"/><path d="M15.5 9a4 4 0 1 0 0 6"/></svg>
    Copyright Copper Ridge Reserves, LLC © 2017 All Rights Reserved
  </footer>
</body>
</html>
```